Construction Directory Website Flyer

We need a postcard size +/- or somewhere around that size (something standard) flyer designed for our construction directory website. Leave a spot for tagline. Call to action is 'register your company now'. I am thinking many mini pictures of different construction to show that it is for the entire construction industry. Logo and screenshot of the homepage of the website is attached. Use same theme as webpage.

Target Market(s)

Construction Industry

Industry/Entity Type

Construction

Font styles to use
Sans Serif

Requirements
Must have
• Call to action
• Colors to match logo
• Area to add description and details.
Nice to have
• Construction Images
Should not have
• No Cartoonish types of things

```html
<!DOCTYPE html>
<html lang="en">
<head>
<meta charset="utf-8">
<title>BuildLink Hub – Register Your Company Flyer</title>
<link href="https://fonts.googleapis.com/css2?family=Oswald:wght@500&family=Lato:wght@400;700&family=Montserrat:wght@700;800&display=swap" rel="stylesheet">
<style>
  :root{
    --slate:#4b515c;
    --slate-dark:#3d424c;
    --red:#e0262b;
    --orange:#f07f1e;
    --panel:#efece8;
    --ink:#2f3137;
    --white:#ffffff;
  }
  html,body{margin:0;padding:0;overflow:hidden;background:#2b2d31;}
  .flyer{position:relative;width:1200px;height:902px;overflow:hidden;font-family:'Lato',sans-serif;}
  .flyer-shapes{position:absolute;inset:0;width:1200px;height:902px;display:block;}
  .brand{position:absolute;left:150px;top:37px;width:480px;height:148px;display:flex;align-items:center;justify-content:center;gap:16px;}
  .brand-mark{width:34px;height:34px;background:var(--orange);}
  .brand-name{font-family:'Montserrat',sans-serif;font-weight:700;font-size:40px;color:var(--slate-dark);letter-spacing:.5px;}
  .headline{position:absolute;left:645px;width:540px;top:64px;margin:0;text-align:center;font-family:'Oswald',sans-serif;font-weight:500;color:var(--white);text-transform:uppercase;line-height:1;white-space:nowrap;}
  .headline-main{display:block;font-size:76px;}
  .headline-sub{display:block;font-size:64px;margin-top:20px;}
  .description{position:absolute;left:640px;top:296px;width:528px;margin:0;font-size:25.5px;line-height:35.5px;color:var(--ink);text-align:justify;text-indent:26px;}
  .cta{position:absolute;left:560px;width:630px;top:606px;margin:0;text-align:center;font-family:'Montserrat',sans-serif;font-weight:800;font-size:33px;color:var(--ink);letter-spacing:.3px;white-space:nowrap;}
  .cta-accent{color:var(--red);}
  .phone{position:absolute;left:590px;width:560px;top:688px;height:60px;display:flex;align-items:center;justify-content:center;gap:12px;font-family:'Montserrat',sans-serif;font-weight:800;font-size:46px;color:var(--white);white-space:nowrap;}
  .phone-icon{width:42px;height:42px;}
  .website{position:absolute;left:560px;width:630px;top:800px;display:flex;align-items:center;justify-content:center;gap:22px;font-family:'Lato',sans-serif;font-weight:700;font-size:24px;letter-spacing:5px;color:var(--white);white-space:nowrap;}
  .globe-icon{width:26px;height:26px;}
</style>
</head>
<body>
<div class="flyer">
  <svg class="flyer-shapes" viewBox="0 0 1076 732" preserveAspectRatio="none">
    <defs>
      <linearGradient id="band" x1="0" x2="1">
        <stop offset="0" stop-color="#e0262b"/><stop offset=".5" stop-color="#f07f1e"/><stop offset="1" stop-color="#e0262b"/>
      </linearGradient>
      <linearGradient id="side-strip" x1="0" y1="0" x2="0" y2="1">
        <stop offset="0" stop-color="#e0262b"/><stop offset="1" stop-color="#f07f1e"/>
      </linearGradient>
      <linearGradient id="panel" x1="0" x2="1">
        <stop offset="0" stop-color="#f6f4f1"/><stop offset="1" stop-color="#e2ddd6"/>
      </linearGradient>
      <linearGradient id="ph-concrete" x1="0" y1="0" x2="0" y2="1"><stop offset="0" stop-color="#c9c6c0"/><stop offset="1" stop-color="#8d8a85"/></linearGradient>
      <linearGradient id="ph-road" x1="0" y1="0" x2="0" y2="1"><stop offset="0" stop-color="#7fb6e6"/><stop offset=".55" stop-color="#6a7a6e"/><stop offset="1" stop-color="#a89a84"/></linearGradient>
      <linearGradient id="ph-tower" x1="0" y1="0" x2="0" y2="1"><stop offset="0" stop-color="#2f78d4"/><stop offset="1" stop-color="#a9c9ea"/></linearGradient>
      <linearGradient id="ph-rebar" x1="0" y1="0" x2="0" y2="1"><stop offset="0" stop-color="#6d6f73"/><stop offset="1" stop-color="#a9a7a1"/></linearGradient>
      <linearGradient id="ph-timber" x1="0" y1="0" x2="0" y2="1"><stop offset="0" stop-color="#c89a5e"/><stop offset="1" stop-color="#e6d27a"/></linearGradient>
      <linearGradient id="ph-digger" x1="0" y1="0" x2="0" y2="1"><stop offset="0" stop-color="#3d7fd6"/><stop offset=".6" stop-color="#d9a52a"/><stop offset="1" stop-color="#8a6a44"/></linearGradient>
    </defs>
    <rect class="body-fill" x="0" y="0" width="1076" height="732" fill="var(--slate)"/>
    <rect class="band-top" x="0" y="0" width="1076" height="30" fill="url(#band)"/>
    <rect class="band-bottom" x="0" y="706" width="1076" height="26" fill="url(#band)"/>
    <polygon class="side-strip" points="0,205 80,205 50,706 0,706" fill="url(#side-strip)"/>
    <polygon class="logo-panel" points="135,30 578,30 545,150 118,150" fill="var(--white)"/>
    <polygon class="logo-slash" points="578,30 592,30 558,150 545,150" fill="var(--orange)"/>
    <polygon class="text-panel" points="488,225 1076,225 1076,562 470,562" fill="url(#panel)"/>
    <g class="photo-grid" stroke="#ffffff" stroke-width="4">
      <g role="img" aria-label="Photo: workers pouring concrete"><polygon points="95,155 300,155 285,330 75,330" fill="url(#ph-concrete)"/></g>
      <g role="img" aria-label="Photo: road paving crew with rollers"><polygon points="310,155 548,155 530,330 295,330" fill="url(#ph-road)"/></g>
      <g role="img" aria-label="Photo: high-rise under construction with cranes"><polygon points="75,345 280,345 262,520 50,520" fill="url(#ph-tower)"/></g>
      <g role="img" aria-label="Photo: worker tying rebar mesh"><polygon points="290,345 525,345 508,520 272,520" fill="url(#ph-rebar)"/></g>
      <g role="img" aria-label="Photo: carpenter on roof timber framing"><polygon points="22,532 245,532 226,702 0,702" fill="url(#ph-timber)"/></g>
      <g role="img" aria-label="Photo: yellow excavator digging"><polygon points="256,532 472,532 452,702 236,702" fill="url(#ph-digger)"/></g>
    </g>
    <polygon class="phone-ribbon" points="510,556 1045,556 1030,580 1010,617 545,617 525,580" fill="url(#band)"/>
  </svg>

  <div class="brand">
    <span class="brand-mark"></span>
    <span class="brand-name">BuildLink Hub</span>
  </div>

  <h1 class="headline">
    <span class="headline-main">Lorem Ipsum Is</span>
    <span class="headline-sub">Simply Dummy Text</span>
  </h1>

  <p class="description">Lorem Ipsum is simply dummy text of the printing and typesetting industry. Lorem Ipsum has been the industry's standard dummy text ever since the 1500s, when an unknown printer took a galley of type and scrambled it to make a type specimen bookt has survived not only five centuries.</p>

  <p class="cta">REGISTER YOUR <span class="cta-accent">COMPANY NOW</span></p>

  <div class="phone">
    <svg class="phone-icon" viewBox="0 0 24 24" aria-hidden="true">
      <circle cx="12" cy="12" r="10.5" fill="none" stroke="#ffffff" stroke-width="1.8"/>
      <path d="M8.6 6.8c.4-.3.9-.2 1.1.2l1 1.9c.2.4.1.8-.2 1.1l-.7.6c.6 1.4 1.7 2.5 3.1 3.1l.6-.7c.3-.3.7-.4 1.1-.2l1.900 1c.4.2.5.7.2 1.1l-.9 1.1c-.4.5-1.1.7-1.7.5-3.2-1-5.7-3.5-6.7-6.7-.2-.6 0-1.3.5-1.700z" fill="#ffffff"/>
    </svg>
    <span class="phone-number">000-123-4567-890</span>
  </div>

  <div class="website">
    <svg class="globe-icon" viewBox="0 0 24 24" aria-hidden="true">
      <g fill="none" stroke="var(--orange)" stroke-width="2">
        <circle cx="12" cy="12" r="10"/><ellipse cx="12" cy="12" rx="4.5" ry="10"/>
        <line x1="2" y1="12" x2="22" y2="12"/><line x1="4" y1="7" x2="20" y2="7"/><line x1="4" y1="17" x2="20" y2="17"/>
      </g>
    </svg>
    <span class="website-url">www.websiteaddress.com</span>
  </div>
</div>
</body>
</html>
```